High Tech Software Startup needs Letterhead Design

We need a letterhead for a startup company base in Brazil. The letterhead should combine with our logo attached here.
We are a team of professionals in Java for web and mobile with iOS and android development.
We are looking for a modern and futuristc design.

Target Market(s)

CIO, IT managers of mid to big size companies

Industry/Entity Type

It Company

```html
<!DOCTYPE html>
<html lang="pt-BR">
<head>
<meta charset="utf-8">
<title>Veltra Letterhead</title>
<link rel="stylesheet" href="https://fonts.googleapis.com/css2?family=Fira+Sans:wght@500;700&family=Fira+Sans+Condensed:wght@700&display=swap">
<style>
  :root {
    --backdrop: #e6e6e4;
    --paper: #ffffff;
    --brand-navy: #12365e;
    --brand-blue: #1a7fc0;
    --contact-grey: #4d5560;
    --footer-navy: #0f2a4a;
    --mark-light: #c7e6f7;
    --mark-lilac: #c2c0d6;
  }
  html, body {
    margin: 0;
    padding: 0;
    width: 1039px;
    height: 1200px;
    overflow: hidden;
    background: var(--backdrop);
  }
  .letterhead {
    position: absolute;
    left: 110px;
    top: 23px;
    width: 820px;
    height: 1154px;
    background: var(--paper);
    box-shadow: 0 2px 10px rgba(0,0,0,0.12);
  }
  .brand {
    position: absolute;
    left: 38px;
    top: 38px;
    display: flex;
    align-items: center;
    gap: 18px;
  }
  .brand-square {
    width: 84px;
    height: 84px;
    border-radius: 8px;
    background: var(--brand-blue);
  }
  .brand-name {
    font-family: "Fira Sans", sans-serif;
    font-weight: 700;
    font-size: 94px;
    line-height: 1;
    letter-spacing: 1px;
    color: var(--brand-navy);
  }
  .contact {
    position: absolute;
    left: 548px;
    top: 50px;
    margin: 0;
    font-family: "Fira Sans", sans-serif;
    font-weight: 500;
    font-size: 16px;
    line-height: 21.5px;
    color: var(--contact-grey);
  }
  .backdrop-mark {
    position: absolute;
    left: 219px;
    top: 380px;
    width: 404px;
    height: 404px;
    border-radius: 54px;
    background: linear-gradient(45deg, var(--mark-light) 0%, var(--mark-lilac) 100%);
  }
  .address {
    position: absolute;
    left: 38px;
    top: 1098px;
    margin: 0;
    font-family: "Fira Sans Condensed", sans-serif;
    font-weight: 700;
    font-size: 14.5px;
    line-height: 17px;
    color: var(--footer-navy);
    font-style: normal;
    white-space: pre;
  }
</style>
</head>
<body>
  <main class="letterhead">
    <header class="brand">
      <div class="brand-square"></div>
      <span class="brand-name">VELTRA</span>
    </header>
    <p class="contact">
      Phone: (11) 5555-0142<br>
      Website: www.veltra.com.br<br>
      E-mail: contato@veltra.com.br
    </p>
    <div class="backdrop-mark" aria-hidden="true"></div>
    <address class="address">Rua Augusta, 1480  13°. Andar  Conj. 1207  Caixa Postal  218
Consolação    CEP  01.305-100
São Paulo - SP - Brasil</address>
  </main>
</body>
</html>
```